Footwear & Apparel Business to Business Presentation (B2B)

We are looking for a Business to Business presentation that is simple, clean, and easy to understand.

We would like the steps to be laid out with simple graphics indicating steps 1, 2 , 3 with circles / arrows. Colours are acceptable. This is a tool to engage potential customers so needs to be very clear and easy to understand.

our logo is attached.
Updates

Target Market(s)

women aged 30 plus

Industry/Entity Type

Business

Font styles to use
Serif
Sans Serif

Requirements
Must have
• 2 pages:
• 1st page should be our logo and who we are:
• Coral Ridge Of Textiles
• contact: info@crot.com.au
• We are a wholesale and distribution company of footwear and apparel
• We specialize in clearing aged stock through flash sales channels in Australia and New Zealand.
• We offer suppliers an alternative inventory distribution channel.
• Take advantage of the reverse seasonality - when you can't move your winter stock, We Can!
• presentation black and white
• must look clean , simple , contemporary
• 2nd Page:
• clear detailed step by step process
• graphics demonstrating this
• suggestions:
• step by step on an pebble flatscreen with an arrow between each step with an image on each screen and notes on the side
• we need the following 3 steps on our brief:
• 1 - we buy upfront and handle all processes
• 2 - $ in your bank
• 3 - goods shipped to Australia / New Zealand
Nice to have
• suggestions:
• -use graphics to show moving stock from north america to australia & New zealand
• -maybe a global map
• -icons showing money and transportation
• -demonstrate the 3 steps in pebble windows
• - show the graphics / icons as a backdrop and text on top

```html
<!DOCTYPE html>
<html lang="en">
<head>
<meta charset="utf-8">
<title>Coral Ridge Of Textiles – Page 1</title>
<link rel="stylesheet" href="https://fonts.googleapis.com/css2?family=PT+Sans+Narrow:wght@400;700&family=Raleway:wght@600&display=swap">
<style>
  :root {
    --board-light: #f7f7f7;
    --board-dark: #e3e3e4;
    --paper: #ffffff;
    --ink: #2b2b2b;
    --ink-soft: #3a3a3a;
    --gold: #e2c382;
    --tab: #1f1f1f;
    --tab-text: #ffffff;
  }
  * { margin: 0; padding: 0; box-sizing: border-box; }
  html, body { width: 1200px; height: 1000px; overflow: hidden; }
  body {
    position: relative;
    background: radial-gradient(ellipse at 45% 45%, var(--board-light) 0%, var(--board-dark) 100%);
    font-family: "PT Sans Narrow", "Arial Narrow", sans-serif;
    color: var(--ink);
  }
  .page {
    position: absolute;
    left: 148px; top: 50px;
    width: 637px; height: 900px;
    background: var(--paper);
  }
  .hero {
    position: absolute; left: 0; top: 0;
    width: 637px; height: 282px;
    background: linear-gradient(90deg,
      #b8b2ad 0%, #7a5a45 10%, #2c2a2c 20%, #5b4a42 30%,
      #b8403a 38%, #2a2829 48%, #a8303a 56%, #d9c24a 64%,
      #2d3550 72%, #d8d6d2 82%, #8e86a4 92%, #c9c6c0 100%);
  }
  .hero-band {
    position: absolute; left: 0; top: 282px;
    width: 637px; height: 8px;
    background: var(--gold);
  }
  .brand {
    position: absolute; left: 0; top: 318px;
    width: 637px;
    display: flex; align-items: center; justify-content: center; gap: 16px;
  }
  .brand-mark {
    width: 22px; height: 22px;
    border: 2px solid var(--ink);
    border-radius: 50%;
  }
  .brand-name {
    font-family: "PT Sans Narrow", "Arial Narrow", sans-serif;
    font-weight: 700;
    font-size: 15px;
    letter-spacing: 9px;
    color: var(--ink);
  }
  .tagline {
    position: absolute; left: 0; top: 409px;
    width: 637px;
    text-align: center;
    font-size: 16px;
    line-height: 22px;
    color: var(--ink-soft);
  }
  .about {
    position: absolute; left: 60px; top: 528px;
    width: 540px;
  }
  .about-title {
    font-weight: 700;
    font-size: 19px;
    line-height: 25px;
  }
  .about-list {
    list-style: none;
    margin-top: 4px;
  }
  .about-list li {
    position: relative;
    padding-left: 25px;
    font-size: 18.5px;
    line-height: 28px;
  }
  .about-list li::before {
    content: "";
    position: absolute; left: 2px; top: 10px;
    width: 9px; height: 9px;
    border-radius: 50%;
    background: var(--ink);
  }
  .page-tab {
    position: absolute; left: 901px; top: 422px;
    width: 299px; height: 91px;
    background: var(--tab);
    color: var(--tab-text);
    font-family: Arial, Helvetica, sans-serif;
    font-size: 44px;
    line-height: 91px;
    padding-left: 40px;
  }
  .page-tab strong { font-weight: 700; }
</style>
</head>
<body>
  <section class="page">
    <div class="hero" role="img" aria-label="Row of eleven women modelling dresses and casual outfits in black, red, yellow, navy, white and floral prints"></div>
    <div class="hero-band"></div>

    <div class="brand">
      <span class="brand-mark"></span>
      <span class="brand-name">CORAL RIDGE OF TEXTILES</span>
    </div>

    <p class="tagline">
      "The Coral Ridge of Textiles<br>
      is revolutionizing retail and leading the world more beautiful,<br>
      people say you cant buy style, well at least now you can afford it! "
    </p>

    <div class="about">
      <p class="about-title">Coral Ridge Of Textiles</p>
      <p class="about-title">Contact: info@crot.com.au</p>
      <ul class="about-list">
        <li>We are a wholesale and distribution company of footwear and apparel</li>
        <li>We specialize in clearing aged stock through flash sales channels in Australia and New Zealand.</li>
        <li>We offer suppliers an alternative inventory distribution channel.</li>
        <li>Take advantage of the reverse seasonality</li>
        <li>When you can't move your winter stock, We Can!</li>
        <li>We have access to a data base of over 10 Million shoppers</li>
        <li>Clearing your excess stock through Australia keeps your local retails happy</li>
        <li>We use Tarnwell Freight USA to distribute straight to the Australian and NZ Customer</li>
      </ul>
    </div>
  </section>

  <div class="page-tab">Page <strong>1</strong></div>
</body>
</html>
```